Business Cards

Simple but professional looking business cards

Name: Rina Tolvardi
Title: Principle Nexus Applications Consultant
Email: r@kbrx.net.au
web : www.kbrx.net.au
Phone: +61.8.95203417
Mobile: +61.431862055
Updates

Hi All, Please include the office address Level 1, 200 Quarrington St, Kelmont Heights, WA, 6091

Industry/Entity Type

Business

```html
<!DOCTYPE html>
<html lang="en">
<head>
<meta charset="utf-8">
<title>KBRX Business Card</title>
<link href="https://fonts.googleapis.com/css2?family=Josefin+Sans:wght@300;400;600&display=swap" rel="stylesheet">
<style>
  :root {
    --page-bg: #f4f5f6;
    --card-front: #eceef0;
    --card-back: #3797db;
    --brand-blue: #1e64b4;
    --white: #ffffff;
    --badge-red: #e8211d;
  }
  * { margin: 0; padding: 0; box-sizing: border-box; }
  html, body {
    width: 1200px; height: 931px; overflow: hidden;
    background: var(--page-bg);
    font-family: "Josefin Sans", sans-serif;
  }
  .card-set {
    position: absolute; left: 0; top: 292px;
    width: 1200px; height: 347px; display: flex;
  }
  .card { position: relative; width: 600px; height: 347px; }
  .card-front {
    background: radial-gradient(ellipse at 45% 45%, #ffffff 0%, var(--card-front) 75%);
    display: flex; align-items: center; justify-content: center;
  }
  .brand {
    display: flex; align-items: center; gap: 14px;
    color: var(--brand-blue);
  }
  .brand-dot {
    width: 56px; height: 56px; border-radius: 50%;
    background: var(--brand-blue);
  }
  .brand-name {
    font-size: 64px; font-weight: 400; letter-spacing: 2px;
    line-height: 1; padding-top: 8px;
  }
  .card-back { background: var(--card-back); color: var(--white); }
  .holder {
    position: absolute; left: 30px; top: 142px; width: 340px; text-align: center;
  }
  .holder-name {
    font-size: 31px; font-weight: 600; letter-spacing: 2.5px;
    text-transform: uppercase; line-height: 1;
  }
  .holder-title {
    margin-top: 4px; font-size: 11px; font-weight: 300;
    letter-spacing: 0.4px; text-transform: uppercase;
  }
  .contact {
    position: absolute; left: 411px; top: 88px;
    font-size: 15px; font-weight: 300; letter-spacing: 0.8px; line-height: 20px;
  }
  .contact .web { margin-bottom: 10px; }
  .contact .phone { display: flex; align-items: center; gap: 6px; }
  .icon {
    display: inline-flex; align-items: center; justify-content: center;
    width: 13px; height: 13px; background: var(--white); color: var(--card-back);
    font-size: 10px; font-weight: 600; padding-top: 2px;
  }
  .contact .address { margin-top: 4px; line-height: 18px; }
  .partner-badge {
    position: absolute; left: 26px; top: 290px;
    width: 114px; height: 26px; background: var(--badge-red);
  }
</style>
</head>
<body>
  <main class="card-set">
    <section class="card card-front">
      <div class="brand">
        <span class="brand-dot"></span>
        <span class="brand-name">KBRX</span>
      </div>
    </section>
    <section class="card card-back">
      <div class="holder">
        <h1 class="holder-name">Rina Tolvardi</h1>
        <p class="holder-title">Principle Nexus Applications Consultant</p>
      </div>
      <div class="contact">
        <p>r@kbrx.net.au</p>
        <p class="web">www.kbrx.net.au</p>
        <p class="phone"><span class="icon">P</span>+61.8.95203417</p>
        <p class="phone"><span class="icon">M</span>+61.431862055</p>
        <p class="address">Level 1<br>200 Quarrington St<br>Kelmont Heights, WA<br>6091</p>
      </div>
      <div class="partner-badge" role="img" aria-label="Partner badge"></div>
    </section>
  </main>
</body>
</html>
```